Letterhead design for ZENTORA company

I need an A4 letterhead design for my company "Zentora Electrical Products". I need the letterhead to match my current logo and business card designs. I would like it to be colourful and match the design of the business card in terms of the flowing line of colour where the information is.  

Target Market(s)

Adults aged 20 - 50 Upper middle class.

Industry/Entity Type

It Company

Requirements
Must have
• Must be A4 size and match my current logo and business card designs. Must be clean simple and eye catching.

• Must have the following information

• Zentora Electrical Products LTD
• 7 Ardley Close
• Chiswick
• London
• England
• W9 3QX
• Company No. 05316429
• VAT No. GB 627150384

• Telephone: 02081594360
• Mobile: 07815062247
• Email: info@zentora-goods.co.uk
Nice to have
• nice to have a wave of colour like the business card.
Should not have
• Should not be a different colour scheme to the business card and logo design.

```html
<!DOCTYPE html>
<html lang="en">
<head>
<meta charset="utf-8">
<title>Zentora Electrical Products – Letterhead</title>
<link rel="stylesheet" href="https://fonts.googleapis.com/css2?family=Carlito:wght@400&display=swap">
<style>
  :root {
    --teal-deep: #13929e;
    --teal-mid: #2fb8c0;
    --cyan-bright: #6ff5ee;
    --cyan-soft: #45d2d2;
    --grey-light: #f4f4f4;
    --grey-mid: #d2d2d2;
    --ink: #333333;
    --label-blue: #2a8fd6;
    --paper: #ffffff;
    --backdrop: #ffffff;
  }
  * { box-sizing: border-box; margin: 0; padding: 0; }
  html, body {
    width: 1200px;
    height: 842px;
    overflow: hidden;
    background: var(--backdrop);
  }
  .sheet-set {
    position: relative;
    width: 1200px;
    height: 842px;
  }
  .letterhead {
    position: absolute;
    top: 0;
    width: 599px;
    height: 842px;
    background: var(--paper);
    overflow: hidden;
    font-family: "Carlito", "Calibri", sans-serif;
  }
  .letterhead--plain { left: 0; }
  .letterhead--alt { left: 601px; }
  .letterhead__art {
    position: absolute;
    inset: 0;
    width: 100%;
    height: 100%;
  }
  .brand {
    position: absolute;
    left: 22px;
    top: 14px;
    color: var(--paper);
    font-family: "Carlito", "Calibri", sans-serif;
    font-weight: 400;
    line-height: 1;
  }
  .brand__name {
    display: block;
    font-size: 30px;
    letter-spacing: 1px;
  }
  .brand__name-rest {
    display: block;
    font-size: 13px;
    margin-top: 3px;
    letter-spacing: 0.3px;
  }
  .contact {
    position: absolute;
    left: 38px;
    top: 764px;
    font-size: 8.6px;
    line-height: 15.3px;
    color: var(--ink);
    list-style: none;
  }
  .contact__label {
    color: var(--label-blue);
  }
  .contact__gap {
    display: inline-block;
    width: 10px;
  }
</style>
</head>
<body>
<main class="sheet-set">

  <section class="letterhead letterhead--plain" aria-label="Letterhead, plain version">
    <svg class="letterhead__art" viewBox="0 0 599 842" aria-hidden="true">
      <defs>
        <linearGradient id="headerTeal" x1="0" y1="0" x2="1" y2="1">
          <stop offset="0" stop-color="#17a2ab"/>
          <stop offset="1" stop-color="#12858f"/>
        </linearGradient>
        <linearGradient id="headerCyan" x1="0" y1="0" x2="1" y2="0">
          <stop offset="0" stop-color="#3cc8cc"/>
          <stop offset="1" stop-color="#7ff2ea"/>
        </linearGradient>
        <linearGradient id="footerGrey" x1="0" y1="0" x2="0" y2="1">
          <stop offset="0" stop-color="#d0d0d0"/>
          <stop offset="1" stop-color="#f6f6f6"/>
        </linearGradient>
        <linearGradient id="footerTeal" x1="0" y1="0" x2="1" y2="0">
          <stop offset="0" stop-color="#138d98"/>
          <stop offset="0.5" stop-color="#2fb7bf"/>
          <stop offset="1" stop-color="#158f9a"/>
        </linearGradient>
        <linearGradient id="footerHighlight" x1="0" y1="0" x2="1" y2="0">
          <stop offset="0" stop-color="#3fcfd0"/>
          <stop offset="0.55" stop-color="#7ffcf2"/>
          <stop offset="1" stop-color="#3fcfd0"/>
        </linearGradient>
      </defs>
      <!-- header band -->
      <polygon points="0,0 306,0 180,73 0,73" fill="url(#headerTeal)"/>
      <polygon points="0,50 245,36 180,73 0,73" fill="url(#headerCyan)" opacity="0.85"/>
      <!-- footer wave -->
      <path d="M0,576 C90,700 250,772 400,776 C480,778 555,758 599,734 L599,842 L0,842 Z" fill="url(#footerGrey)"/>
      <path d="M0,576 C90,700 250,772 400,776 C480,778 555,758 599,734 L599,750 C560,772 480,796 400,796 C240,794 80,740 0,648 Z" fill="url(#footerTeal)"/>
      <path d="M0,606 C90,716 250,780 400,784 C480,786 555,766 599,742 L599,747 C555,772 480,791 400,790 C250,787 90,726 0,624 Z" fill="url(#footerHighlight)"/>
    </svg>

    <div class="brand">
      <span class="brand__name">ZENTORA</span>
      <span class="brand__name-rest">Electrical Products</span>
    </div>

    <ul class="contact">
      <li><span class="contact__label">P:</span>02081594360<span class="contact__gap"></span><span class="contact__label">M:</span>07815062247</li>
      <li><span class="contact__label">A:</span>7 Ardley Close, Chiswick, London, England, W9 3QX</li>
      <li><span class="contact__label">E:</span>info@zentora-goods.co.uk<span class="contact__gap"></span><span class="contact__label">W:</span>www.zentora-goods.co.uk</li>
      <li>Zentora Electrical Products LTD<span class="contact__gap"></span>Company No. 05316429<span class="contact__gap"></span>VAT No. GB 627150384</li>
    </ul>
  </section>

  <section class="letterhead letterhead--alt" aria-label="Letterhead, alternate version">
    <svg class="letterhead__art" viewBox="0 0 599 842" aria-hidden="true">
      <polygon points="0,0 306,0 180,73 0,73" fill="url(#headerTeal)"/>
      <polygon points="0,50 245,36 180,73 0,73" fill="url(#headerCyan)" opacity="0.85"/>
      <path d="M0,576 C90,700 250,772 400,776 C480,778 555,758 599,734 L599,842 L0,842 Z" fill="url(#footerGrey)"/>
      <path d="M0,576 C90,700 250,772 400,776 C480,778 555,758 599,734 L599,750 C560,772 480,796 400,796 C240,794 80,740 0,648 Z" fill="url(#footerTeal)"/>
      <path d="M0,606 C90,716 250,780 400,784 C480,786 555,766 599,742 L599,747 C555,772 480,791 400,790 C250,787 90,726 0,624 Z" fill="url(#footerHighlight)"/>
    </svg>

    <div class="brand">
      <span class="brand__name">ZENTORA</span>
      <span class="brand__name-rest">Electrical Products</span>
    </div>

    <ul class="contact">
      <li><span class="contact__label">P:</span>02081594360<span class="contact__gap"></span><span class="contact__label">M:</span>07815062247</li>
      <li><span class="contact__label">A:</span>7 Ardley Close, Chiswick, London, England, W9 3QX</li>
      <li><span class="contact__label">E:</span>info@zentora-goods.co.uk<span class="contact__gap"></span><span class="contact__label">W:</span>www.zentora-goods.co.uk</li>
      <li>Zentora Electrical Products LTD<span class="contact__gap"></span>Company No. 05316429<span class="contact__gap"></span>VAT No. GB 627150384</li>
    </ul>
  </section>

</main>
</body>
</html>
```